Business Card for Financial Asset Management Company

Now we are launching a new company based in Tokyo.
The company information is below;

Company Name: Talvane Management

Operations: Financial assets management, Proposing forming portfolio of assets, Consulting service, and advising to enhance your company's financial health

Corporate Colour: Japan Blue or Navy like below
http://staffpages.qorvenly.edu/mtavis/images/Slate/Teal-Slate-217.jpg

It's dark and deep, and will get to fit to our clients as our relationships last longer and longer.

Our images for this colour are "Japanese style" and "pride in our craftmanship" , and also "gentle".

Corporate Key Image: an order taker who is sincere, polite, but courageous

We don't have our logo yet so please feel free to put any symbol on your design.

Please do not hesitate about asking any questions.
Thank you :-)

Reason: We are still discussin on final decision. Thank you for your understanding.

```html
<!DOCTYPE html>
<html lang="en">
<head>
<meta charset="utf-8">
<title>Talvane Management – Business Card</title>
<link rel="stylesheet" href="https://fonts.googleapis.com/css2?family=Open+Sans:wght@400;500;600&display=swap">
<style>
  :root {
    --japan-blue-deep: #0a4fa6;
    --japan-blue-mid: #0b63bd;
    --japan-blue-light: #1478cf;
    --ink-blue: #0b4f9e;
    --paper: #ffffff;
    --shadow-grey: #dfe0e3;
    --rule-grey: #d6d6d6;
    --text-grey: #666666;
  }
  html, body {
    margin: 0;
    padding: 0;
    overflow: hidden;
    background: var(--paper);
  }
  .card {
    position: relative;
    width: 1200px;
    height: 726px;
    background: var(--paper);
    overflow: hidden;
    font-family: "Open Sans", Arial, sans-serif;
  }
  .card__backdrop {
    position: absolute;
    inset: 0;
    width: 1200px;
    height: 726px;
  }
  .brand {
    position: absolute;
    left: 0;
    top: 142px;
    width: 1200px;
    text-align: center;
    color: var(--paper);
    font-weight: 500;
  }
  .brand__mark {
    width: 132px;
    height: 132px;
    margin: 0 auto 14px;
    border-radius: 50%;
    background: var(--paper);
  }
  .brand__name-main {
    display: block;
    font-size: 64px;
    line-height: 68px;
    letter-spacing: 0.5px;
  }
  .brand__name-sub {
    display: block;
    font-size: 48px;
    line-height: 54px;
  }
  .services {
    position: absolute;
    left: 0;
    top: 533px;
    width: 1200px;
    margin: 0;
    text-align: center;
    font-size: 29px;
    font-weight: 600;
    color: var(--ink-blue);
  }
  .divider {
    position: absolute;
    left: 400px;
    top: 594px;
    width: 400px;
    height: 2px;
    background: var(--rule-grey);
  }
  .website {
    position: absolute;
    left: 0;
    top: 610px;
    width: 1200px;
    text-align: center;
    font-size: 25px;
    font-weight: 400;
    color: var(--text-grey);
  }
</style>
</head>
<body>
<div class="card">
  <svg class="card__backdrop" viewBox="0 0 1200 726" xmlns="http://www.w3.org/2000/svg">
    <defs>
      <radialGradient id="waveFill" cx="0.5" cy="0.45" r="0.7">
        <stop offset="0" stop-color="var(--japan-blue-light)"/>
        <stop offset="0.6" stop-color="var(--japan-blue-mid)"/>
        <stop offset="1" stop-color="var(--japan-blue-deep)"/>
      </radialGradient>
    </defs>
    <path class="band-shadow" d="M0,385 Q600,565 1200,385 L1200,397 Q600,587 0,397 Z" fill="var(--shadow-grey)"/>
    <path class="band-pattern" role="img" aria-label="Japanese wave pattern of overlapping concentric arcs in Japan blue"
          d="M0,0 H1200 V385 Q600,565 0,385 Z" fill="url(#waveFill)"/>
  </svg>

  <div class="brand">
    <div class="brand__mark"></div>
    <span class="brand__name-main">Talvane</span>
    <span class="brand__name-sub">Management</span>
  </div>

  <p class="services">Financial Assets . Proposing Porfolio . Consulting Services</p>
  <div class="divider"></div>
  <div class="website">www.talvanemanagement.jp</div>
</div>
</body>
</html>
```